Упаковка для Bright Vega
Задание на дизайн
Приоритеты объектов в упаковке
Зонтичная марка, Знак производителя, Марка продукта, Вид продукта, Название продукта, Иллюстрация
Размеры
Опишите свою организацию или продукт и целевую аудиторию
Производство и продажа электро-, бензо-, аккумуляторного инструмента для строительства и ремонта.
Существующая упаковка .То, что хочется обновить.
Образец существующей упаковки.
Комментарии и пожелания для дизайнеров
Необходимо полностью обновить устаревший дизайн упаковки для инструмента, на примере шуруповерта. Фирменный красный цвет, а также сам логотип и сочетания цветов внутри него менять нельзя. Логотип обязательно должен присутствовать на упаковке. Название серии Zet power line должно остаться, но в любом другом виде и написании. Остальное можно менять до неузнаваемости. Фото инструмента должно быть помещено на упаковку целиком. Упаковка должна быть современной, сочной, красочной, информативной и обязательно несложно адаптивной под другие виды инструмента и форматы коробок (ушм, перфораторы, лобзики и пр.). Другие образцы наших упаковок можно легко найти в сети.

```html
<!DOCTYPE html>
<html lang="en">
<head>
<meta charset="utf-8">
<title>Bright Vega — Screwdriver Packaging</title>
<link rel="stylesheet" href="https://fonts.googleapis.com/css2?family=Montserrat:wght@700;800&family=Oswald:wght@700&display=swap">
<style>
  :root {
    --brand-red: #c8261b;
    --ink: #1c1c1c;
    --paper: #f7f6f3;
    --backdrop: #e9e9ea;
    --window: #ededee;
    --strip: #232323;
  }
  * { margin: 0; padding: 0; box-sizing: border-box; }
  html, body {
    width: 1200px; height: 1200px; overflow: hidden;
    background: var(--backdrop);
  }
  .canvas { position: relative; width: 1200px; height: 1200px; }
  .box-front {
    position: absolute; left: 80px; top: 80px;
    width: 1040px; height: 1040px;
    background: var(--paper);
    overflow: hidden;
  }
  .side-strip {
    position: absolute; right: 0; top: 40px;
    width: 200px; height: 960px;
    background: var(--strip);
  }
  .brand-block {
    position: absolute; left: 0; top: 0;
    width: 470px; height: 220px;
    background: var(--brand-red);
    padding: 52px 0 0 48px;
  }
  .brand-name {
    font-family: "Montserrat", sans-serif;
    font-weight: 800;
    font-size: 58px;
    line-height: 1.02;
    color: #fff;
    text-transform: uppercase;
  }
  .series-name {
    position: absolute; left: 48px; top: 256px;
    font-family: "Montserrat", sans-serif;
    font-weight: 800;
    font-size: 28px;
    letter-spacing: 0.06em;
    color: var(--brand-red);
    text-transform: uppercase;
  }
  .product-type {
    position: absolute; left: 48px; top: 310px;
    font-family: "Oswald", sans-serif;
    font-weight: 700;
    font-size: 128px;
    line-height: 1;
    color: var(--ink);
    text-transform: uppercase;
  }
  .spec-band {
    position: absolute; left: 0; top: 600px;
    width: 640px; height: 150px;
    background: var(--brand-red);
    clip-path: polygon(0 0, 500px 0, 640px 150px, 0 150px);
    padding: 34px 0 0 48px;
  }
  .spec-line {
    font-family: "Montserrat", sans-serif;
    font-weight: 700;
    font-size: 34px;
    line-height: 1.3;
    color: #fff;
    text-transform: uppercase;
  }
  .spec-line--power { text-transform: none; }
  .accent-stripe {
    position: absolute; left: 0; top: 830px;
    width: 520px; height: 34px;
    background: var(--brand-red);
  }
  .base-band {
    position: absolute; left: 0; bottom: 0;
    width: 100%; height: 62px;
    background: var(--brand-red);
  }
  .product-window {
    position: absolute; left: 500px; top: 150px;
    width: 440px; height: 700px;
    border-radius: 14px;
    background: linear-gradient(160deg, #f4f4f4, var(--window));
    box-shadow: inset 0 0 0 3px #d9d6d0;
    overflow: hidden;
  }
  .window-photo {
    position: absolute; left: 0; top: 30px;
    width: 92%; height: 640px;
    border-radius: 0 40px 40px 0;
    background: linear-gradient(150deg, #2a2a2a 0%, #d9321f 30%, #c8261b 60%, #2a2a2a 100%);
  }
  .thumb-photo {
    position: absolute; left: 130px; top: 770px;
    width: 340px; height: 270px;
    border-radius: 6px;
    background: linear-gradient(110deg, #2a2a2a 0%, #3a3a3a 45%, #c8261b 75%, #d9321f 100%);
  }
</style>
</head>
<body>
<div class="canvas">
  <section class="box-front">
    <div class="side-strip"></div>

    <div class="brand-block">
      <p class="brand-name">Bright<br>Vega</p>
    </div>

    <p class="series-name">Zet power line</p>
    <h1 class="product-type">Screw<br>Driver</h1>

    <div class="spec-band">
      <p class="spec-line spec-line--power">18V · 2 × 2.0Ah · 10mm</p>
      <p class="spec-line">Variable Speed</p>
    </div>

    <div class="accent-stripe"></div>
    <div class="base-band"></div>

    <div class="product-window">
      <div class="window-photo" role="img" aria-label="Product photo: red and black cordless screwdriver, full view"></div>
    </div>

    <div class="thumb-photo" role="img" aria-label="Product photo: cordless screwdriver side view with chuck and bit"></div>
  </section>
</div>
</body>
</html>
```